Urine collection cup with and without sterile seal sticker

Hello. We need a urine cup label designed please with

Name:
Date of Birth:
Date:
Time:
Temp℃:
Specimen ID:

Product code: TUB-47
Volume markings (e.g., 30 mL, 60 mL, 90 mL).
Vela Drug Tests logo

Could you please provide one version with the additional sterile sticker extending to the top, and one version without the additional sterile sticker?

```html
<!DOCTYPE html>
<html lang="en">
<head>
<meta charset="utf-8">
<title>Specimen Cup Labels – Vela Drug Tests</title>
<link href="https://fonts.googleapis.com/css2?family=Roboto+Condensed:wght@400;500;700&display=swap" rel="stylesheet">
<style>
  :root {
    --navy: #1d3466;
    --navy-deep: #172b57;
    --green: #6aaa3f;
    --label-white: #ffffff;
    --page: #f3f5f9;
    --edge: #d5dbe6;
  }
  * { box-sizing: border-box; margin: 0; padding: 0; }
  html, body { width: 1200px; height: 800px; overflow: hidden; }
  body {
    background: var(--page);
    font-family: "Roboto Condensed", Arial, sans-serif;
    color: var(--navy);
    position: relative;
  }
  .version-title {
    position: absolute;
    top: 22px;
    width: 500px;
    text-align: center;
    font-weight: 700;
    font-size: 28px;
    letter-spacing: 0.5px;
    color: var(--navy);
  }
  .version-title--sterile { left: 70px; }
  .version-title--plain { left: 630px; }

  .cup-label {
    position: absolute;
    top: 200px;
    width: 500px;
    height: 520px;
    background: var(--label-white);
    border: 1px solid var(--edge);
    border-radius: 14px;
    overflow: hidden;
  }
  .cup-label--sterile { left: 70px; }
  .cup-label--plain { left: 630px; }

  .field-list {
    position: absolute;
    left: 26px;
    top: 30px;
    width: 300px;
  }
  .field {
    display: flex;
    align-items: flex-end;
    height: 30px;
    margin-bottom: 31px;
    font-size: 22px;
    font-weight: 500;
    color: var(--navy);
  }
  .field__rule {
    flex: 1;
    margin-left: 10px;
    margin-bottom: 4px;
    border-bottom: 1.5px solid var(--navy);
  }

  .volume-scale {
    position: absolute;
    left: 352px;
    top: 20px;
  }

  .brand {
    position: absolute;
    left: 26px;
    bottom: 66px;
    display: flex;
    align-items: center;
    gap: 12px;
  }
  .brand__dot {
    width: 26px;
    height: 26px;
    border-radius: 50%;
    background: var(--green);
  }
  .brand__name {
    font-size: 30px;
    font-weight: 700;
    color: var(--navy);
  }

  .product-band {
    position: absolute;
    left: 0; right: 0; bottom: 0;
    height: 44px;
    background: var(--navy);
    color: #fff;
    font-size: 19px;
    font-weight: 500;
    display: flex;
    align-items: center;
    justify-content: center;
  }

  .sterile-seal {
    position: absolute;
    left: 268px;
    top: 66px;
    width: 116px;
    height: 170px;
    background: var(--navy-deep);
    border-radius: 6px 6px 0 0;
    color: #fff;
    text-align: center;
    z-index: 2;
    padding-top: 12px;
  }
  .sterile-seal__title {
    font-size: 24px;
    font-weight: 700;
    letter-spacing: 0.5px;
  }
  .sterile-seal__icon { display: block; margin: 14px auto 10px; }
  .sterile-seal__warning {
    font-size: 14px;
    font-weight: 500;
    line-height: 1.25;
  }
</style>
</head>
<body>

  <h2 class="version-title version-title--sterile">WITH STERILE STICKER</h2>
  <h2 class="version-title version-title--plain">WITHOUT STERILE STICKER</h2>

  <div class="sterile-seal">
    <div class="sterile-seal__title">STERILE</div>
    <svg class="sterile-seal__icon" width="52" height="52" viewBox="0 0 52 52" aria-hidden="true">
      <circle cx="26" cy="26" r="22" fill="none" stroke="#fff" stroke-width="4"/>
      <line x1="11" y1="11" x2="41" y2="41" stroke="#fff" stroke-width="4"/>
    </svg>
    <div class="sterile-seal__warning">DO NOT USE<br>IF SEAL IS<br>BROKEN</div>
  </div>

  <section class="cup-label cup-label--sterile">
    <div class="field-list">
      <div class="field">Name:<span class="field__rule"></span></div>
      <div class="field">Date of Birth:<span class="field__rule"></span></div>
      <div class="field">Date:<span class="field__rule"></span></div>
      <div class="field">Time:<span class="field__rule"></span></div>
      <div class="field">Temp℃:<span class="field__rule"></span></div>
      <div class="field">Specimen ID:<span class="field__rule"></span></div>
    </div>
    <svg class="volume-scale" width="130" height="440" viewBox="0 0 130 440" aria-label="Volume scale 30 to 90 mL">
      <g stroke="#1d3466" stroke-width="1.5">
        <line x1="10" y1="0" x2="10" y2="440"/>
        <line x1="10" y1="40" x2="40" y2="40"/>
        <line x1="10" y1="72" x2="24" y2="72"/>
        <line x1="10" y1="104" x2="24" y2="104"/>
        <line x1="10" y1="136" x2="24" y2="136"/>
        <line x1="10" y1="168" x2="24" y2="168"/>
        <line x1="10" y1="200" x2="40" y2="200"/>
        <line x1="10" y1="232" x2="24" y2="232"/>
        <line x1="10" y1="264" x2="24" y2="264"/>
        <line x1="10" y1="296" x2="24" y2="296"/>
        <line x1="10" y1="328" x2="24" y2="328"/>
        <line x1="10" y1="360" x2="40" y2="360"/>
      </g>
      <g fill="#1d3466" font-family="Roboto Condensed, Arial, sans-serif" font-size="22" font-weight="500">
        <text x="50" y="48">90 mL</text>
        <text x="50" y="208">60 mL</text>
        <text x="50" y="368">30 mL</text>
      </g>
    </svg>
    <div class="brand">
      <span class="brand__dot"></span>
      <span class="brand__name">Vela Drug Tests</span>
    </div>
    <div class="product-band">Product code: TUB-47</div>
  </section>

  <section class="cup-label cup-label--plain">
    <div class="field-list">
      <div class="field">Name:<span class="field__rule"></span></div>
      <div class="field">Date of Birth:<span class="field__rule"></span></div>
      <div class="field">Date:<span class="field__rule"></span></div>
      <div class="field">Time:<span class="field__rule"></span></div>
      <div class="field">Temp℃:<span class="field__rule"></span></div>
      <div class="field">Specimen ID:<span class="field__rule"></span></div>
    </div>
    <svg class="volume-scale" width="130" height="440" viewBox="0 0 130 440" aria-label="Volume scale 30 to 90 mL">
      <g stroke="#1d3466" stroke-width="1.5">
        <line x1="10" y1="0" x2="10" y2="440"/>
        <line x1="10" y1="40" x2="40" y2="40"/>
        <line x1="10" y1="72" x2="24" y2="72"/>
        <line x1="10" y1="104" x2="24" y2="104"/>
        <line x1="10" y1="136" x2="24" y2="136"/>
        <line x1="10" y1="168" x2="24" y2="168"/>
        <line x1="10" y1="200" x2="40" y2="200"/>
        <line x1="10" y1="232" x2="24" y2="232"/>
        <line x1="10" y1="264" x2="24" y2="264"/>
        <line x1="10" y1="296" x2="24" y2="296"/>
        <line x1="10" y1="328" x2="24" y2="328"/>
        <line x1="10" y1="360" x2="40" y2="360"/>
      </g>
      <g fill="#1d3466" font-family="Roboto Condensed, Arial, sans-serif" font-size="22" font-weight="500">
        <text x="50" y="48">90 mL</text>
        <text x="50" y="208">60 mL</text>
        <text x="50" y="368">30 mL</text>
      </g>
    </svg>
    <div class="brand">
      <span class="brand__dot"></span>
      <span class="brand__name">Vela Drug Tests</span>
    </div>
    <div class="product-band">Product code: TUB-47</div>
  </section>

</body>
</html>
```